Makeup Artist Requires Business Card design

Hi

I am looking for a business card design to market my makeup artist business. I operate under my own name Mara Veldt and I would like to keep the design of the card very simplistic and chic - something that keeps both my name and profession (makeup artist) the focus of the card. I would like it to be a style that is eyecatching to the reader (i am open to anything unusual) but upmarket.

Target Market(s)

women, magazine/beauty/fashion editors, photographers.

Industry/Entity Type

Business

Requirements
Must have
• Must contain:

Phone number: 0418 372 915
Website: www.maraveldt.com.au
email: contact@maraveldt.com.au

(although you don't need to have prefaced these with the words phone number, website etc :))
Should not have
• I am not looking for anything overly colorful - my preference is to keep the card dark if possible.

```html
<!DOCTYPE html>
<html lang="en">
<head>
<meta charset="utf-8">
<title>Mara Veldt — Make-up Artist Business Card</title>
<link rel="stylesheet" href="https://fonts.googleapis.com/css2?family=Pinyon+Script&family=Tinos:wght@400&display=swap">
<style>
  :root {
    --stage: #e9e6e3;
    --card-black: #0b0b0d;
    --handle-dark: #17161b;
    --handle-sheen: #4a4752;
    --bristle-pink: #f0529f;
    --bristle-light: #ff86c1;
    --bristle-deep: #a3235f;
    --ink-white: #ffffff;
  }
  * { margin: 0; padding: 0; box-sizing: border-box; }
  html, body {
    width: 1200px;
    height: 900px;
    overflow: hidden;
    background: var(--stage);
  }
  .canvas {
    position: relative;
    width: 1200px;
    height: 900px;
  }
  .business-card {
    position: absolute;
    left: 80px;
    top: 132px;
    width: 1040px;
    height: 636px;
    background: var(--card-black);
    overflow: hidden;
    color: var(--ink-white);
  }
  .brush-artwork {
    position: absolute;
    inset: 0;
    width: 100%;
    height: 100%;
  }
  .artist-name {
    position: absolute;
    left: 0;
    right: 0;
    top: 38px;
    text-align: center;
    font-family: "Pinyon Script", cursive;
    font-size: 138px;
    line-height: 1;
    font-weight: 400;
    letter-spacing: 2px;
  }
  .profession {
    position: absolute;
    left: 0;
    right: 0;
    top: 236px;
    text-align: center;
    font-family: "Tinos", serif;
    font-size: 48px;
    letter-spacing: 1px;
  }
  .phone {
    position: absolute;
    left: 0;
    right: 0;
    top: 338px;
    text-align: center;
    font-family: "Tinos", serif;
    font-size: 56px;
    letter-spacing: 2px;
  }
  .web-contacts {
    position: absolute;
    left: 56px;
    right: 56px;
    bottom: 54px;
    display: flex;
    justify-content: space-between;
    font-family: "Tinos", serif;
    font-size: 30px;
  }
</style>
</head>
<body>
  <main class="canvas">
    <article class="business-card">
      <svg class="brush-artwork" viewBox="0 0 1040 636" role="img" aria-label="Close-up photograph of a make-up brush: pink bristles on the left, glossy black handle on the right">
        <defs>
          <linearGradient id="bristle-fill" x1="0" y1="0" x2="0.55" y2="1">
            <stop offset="0" stop-color="var(--bristle-light)"/>
            <stop offset="0.5" stop-color="var(--bristle-pink)"/>
            <stop offset="0.85" stop-color="var(--bristle-deep)"/>
            <stop offset="1" stop-color="var(--card-black)"/>
          </linearGradient>
          <linearGradient id="handle-fill" x1="0" y1="0" x2="0" y2="1">
            <stop offset="0" stop-color="var(--handle-dark)"/>
            <stop offset="0.28" stop-color="var(--handle-sheen)"/>
            <stop offset="0.45" stop-color="var(--handle-dark)"/>
            <stop offset="1" stop-color="var(--card-black)"/>
          </linearGradient>
        </defs>
        <rect class="brush-handle" x="0" y="0" width="1040" height="636" fill="url(#handle-fill)"/>
        <polygon class="brush-bristles" points="0,0 560,0 610,636 0,636" fill="url(#bristle-fill)"/>
      </svg>

      <h1 class="artist-name">Mara Veldt</h1>
      <p class="profession">MAKE-UP ARTIST</p>
      <p class="phone">0418 372 915</p>
      <p class="web-contacts">
        <span class="website">www.maraveldt.com.au</span>
        <span class="email">contact@maraveldt.com.au</span>
      </p>
    </article>
  </main>
</body>
</html>
```